Energieberater sucht Flyer-Design
Zielgruppe
Ich bin Energieberater, habe mich vor kurzem selbstständig gemacht und möchte nun meine Bekanntheit steigern. Meine Zielgruppe sind Immobilieneigentümer sowie Immobiliensuchende, welchen ich eine fundierte Energieberatung mit Sanierungskonzepten sowie die Erstellung von Energieausweisen bieten kann.
Aufgabenstellung
Ich benötige einen Flyer, welchen ich regional verteilen möchte. Der Flyer soll quadratisch (148 x 148) erstellt werden.
Der Flyer sollte mein Logo, meine Kontaktdaten, die unten aufgeführten Dienstleistungen sowie einen Gutschein enthalten und insbesondere der Bekanntheits-/Imagesteigerung dienen.
Vorhandene Punkte sollen sein:
- Erstellung von Energieausweisen für Vermietung und Verkauf
- Energieberatung
- Sanierungs- und Modernisierungskonzepte
- Fördermittelberatung
Der Flyer soll die Möglichkeit bieten, am Rand abgeschnitten zu werden. Dort soll ein Gutschein aufgeführt werden mit 25 € Rabatt für einen Energieausweis.
Meine Kontaktdaten können Sie der angehängten Visitenkarte entnehmen.

```html
<!DOCTYPE html>
<html lang="de">
<head>
<meta charset="utf-8">
<title>Energieberatung Jonas Fehlbach – Flyer</title>
<link href="https://fonts.googleapis.com/css2?family=Roboto+Condensed:wght@400;700&family=Roboto:wght@400;500;700&display=swap" rel="stylesheet">
<style>
  :root {
    --teal: #137a93;
    --teal-text: #1d6e86;
    --orange: #f2a200;
    --white: #ffffff;
    --ink: #2c6f84;
    --photo-dark: #3f5f78;
    --photo-mid: #6f8ea8;
    --photo-light: #a9c3d6;
    --dots: #9fb4bf;
  }
  * { box-sizing: border-box; margin: 0; padding: 0; }
  html, body { width: 1200px; height: 1200px; overflow: hidden; background: var(--white); }
  .flyer { position: relative; width: 1200px; height: 1200px; font-family: "Roboto", Arial, sans-serif; }

  .main { position: absolute; left: 0; top: 0; width: 968px; height: 1200px; }
  .hero-photo {
    position: absolute; left: 0; top: 0; width: 968px; height: 824px;
    background:
      radial-gradient(ellipse 300px 240px at 470px 470px, #f7a21a 0%, #e7852a 45%, rgba(120,160,200,0) 100%),
      radial-gradient(ellipse 420px 320px at 470px 460px, #3a88c2 0%, rgba(60,110,150,0) 100%),
      linear-gradient(180deg, var(--photo-dark) 0%, var(--photo-mid) 60%, var(--photo-light) 100%);
  }
  .hero-band { position: absolute; left: 0; top: 824px; width: 968px; height: 34px; background: var(--teal); }
  .headline {
    position: absolute; left: 55px; top: 76px;
    font-family: "Roboto Condensed", "Arial Narrow", sans-serif; font-weight: 700;
    font-size: 96px; line-height: 1; color: var(--white); letter-spacing: 0.5px;
  }

  .services {
    position: absolute; left: 398px; top: 662px; width: 570px; height: 233px;
    background: var(--orange); border-radius: 12px 0 0 0; color: var(--white);
    padding: 16px 24px 0 24px;
  }
  .services h2 {
    font-family: "Roboto Condensed", "Arial Narrow", sans-serif; font-weight: 700;
    font-size: 32px; line-height: 1.1; margin-bottom: 10px;
  }
  .services ul { list-style: none; font-weight: 500; font-size: 22px; line-height: 30px; }
  .services li { padding-left: 22px; position: relative; }
  .services li::before { content: "-"; position: absolute; left: 2px; }

  .brand { position: absolute; left: 180px; top: 930px; display: flex; align-items: center; gap: 22px; }
  .brand-square { width: 74px; height: 74px; border: 5px solid var(--teal); }
  .brand-name {
    font-family: "Roboto", Arial, sans-serif; font-weight: 500; color: var(--teal);
    font-size: 30px; letter-spacing: 4px; line-height: 1.25; text-transform: uppercase;
  }

  .divider-dots { position: absolute; left: 0; top: 1057px; width: 968px; border-top: 2px dotted var(--dots); }

  .contact { position: absolute; top: 1082px; font-size: 22px; line-height: 31px; color: var(--teal-text); }
  .contact-address { left: 148px; }
  .contact-address strong { font-weight: 700; }
  .contact-reach { left: 412px; }

  .voucher-cut { position: absolute; left: 968px; top: 0; height: 1200px; border-left: 2px dashed var(--dots); }

  .voucher-brand { position: absolute; left: 970px; top: 0; width: 230px; height: 556px; background: var(--white); }
  .vertical { position: absolute; writing-mode: vertical-rl; transform: rotate(180deg); white-space: nowrap; }
  .voucher-brand .brand-name { left: 48px; bottom: 90px; font-size: 24px; letter-spacing: 3px; }
  .voucher-brand .brand-square-small {
    position: absolute; left: 50px; bottom: 28px; width: 44px; height: 44px; border: 4px solid var(--teal);
  }
  .voucher-email { left: 126px; bottom: 80px; font-size: 22px; color: var(--teal-text); }

  .voucher-offer { position: absolute; left: 970px; top: 556px; width: 230px; height: 644px; background: var(--teal); color: var(--white); }
  .voucher-amount {
    left: 28px; bottom: 42px; font-family: "Roboto Condensed", "Arial Narrow", sans-serif;
    font-weight: 700; font-size: 92px; line-height: 1;
  }
  .voucher-note {
    left: 140px; bottom: 40px; font-family: "Roboto Condensed", "Arial Narrow", sans-serif;
    font-weight: 400; font-size: 36px; line-height: 1;
  }
</style>
</head>
<body>
<div class="flyer">
  <section class="main">
    <div class="hero-photo" role="img" aria-label="Foto: Mann im blauen Hemd hält ein Tablet mit einem Haus und einer farbigen Energieeffizienzskala von A bis G"></div>
    <div class="hero-band"></div>
    <h1 class="headline">GUTER RAT SPART GELD</h1>

    <div class="services">
      <h2>MEINE LEISTUNGEN</h2>
      <ul>
        <li>Erstellung von Energieausweisen<br>für Vermietung und Verkauf</li>
        <li>Energieberatung</li>
        <li>Sanierungs- und Modernisierungskonzepte</li>
        <li>Fördermittelberatung</li>
      </ul>
    </div>

    <div class="brand">
      <div class="brand-square"></div>
      <div class="brand-name">Energieberatung<br>Jonas Fehlbach</div>
    </div>

    <div class="divider-dots"></div>

    <address class="contact contact-address" style="font-style:normal">
      <strong>Jonas Fehlbach</strong><br>
      Am Lindenhang 4<br>
      35712 Birkental
    </address>
    <div class="contact contact-reach">
      Tel:&nbsp; +49 0151 47205968<br>
      info@energieberatung-fehlbach.de<br>
      www.energieberatung-fehlbach.de
    </div>
  </section>

  <div class="voucher-cut"></div>

  <aside class="voucher-brand">
    <div class="brand-name vertical">Energieberatung<br>Jonas Fehlbach</div>
    <div class="brand-square-small"></div>
    <div class="voucher-email vertical">info@energieberatung-fehlbach.de</div>
  </aside>

  <aside class="voucher-offer">
    <div class="voucher-amount vertical">25 € RABATT</div>
    <div class="voucher-note vertical">FÜR EINEN ENERGIEAUSWEIS</div>
  </aside>
</div>
</body>
</html>
```